IT Services Company - Company Logo, Flyer design

We are an IT professional services company that provides technical service and support in the residential market. I would like to create a colorful logo and flyer that will be mainly letterbox dropped.

Target Market(s)

residential

Industry/Entity Type

It Company

Requirements
Must have
• nice look and feel, easy to read

```html
<!DOCTYPE html>
<html lang="en">
<head>
<meta charset="utf-8">
<title>Brightlink Home Tech – Flyer</title>
<link href="https://fonts.googleapis.com/css2?family=Noto+Sans:wght@500;600;700&family=Zilla+Slab:wght@500&display=swap" rel="stylesheet">
<style>
  :root {
    --ink: #141414;
    --bullet: #336699;
    --teal-light: #a7d2c8;
    --grey-green: #7d8f86;
    --sage: #b9d0b0;
    --cyan: #00cccc;
    --frame: #a9bca4;
    --band: #a8bba2;
    --white: #ffffff;
  }
  html, body {
    margin: 0;
    width: 1200px;
    height: 1200px;
    overflow: hidden;
    background: var(--white);
  }
  .stage {
    position: absolute;
    left: 0;
    top: 0;
    width: 1500px;
    height: 1500px;
    transform: scale(0.8);
    transform-origin: 0 0;
    font-family: "Noto Sans", sans-serif;
    color: var(--ink);
  }
  .flyer {
    position: absolute;
    left: 230px;
    top: 13px;
    width: 1040px;
    height: 1477px;
    overflow: hidden;
    background:
      radial-gradient(ellipse 520px 380px at 0% 15%, rgba(167,210,200,0.95), rgba(167,210,200,0) 100%),
      radial-gradient(ellipse 700px 420px at 75% 100%, rgba(192,214,178,0.95), rgba(192,214,178,0) 100%),
      radial-gradient(ellipse 400px 300px at 5% 75%, rgba(180,205,175,0.8), rgba(180,205,175,0) 100%),
      linear-gradient(160deg, var(--teal-light) 0%, var(--grey-green) 45%, var(--grey-green) 60%, var(--sage) 100%);
  }
  .company-name {
    position: absolute;
    left: 0;
    top: 160px;
    width: 1040px;
    margin: 0;
    text-align: center;
    font-family: "Zilla Slab", serif;
    font-weight: 500;
    font-size: 54px;
    line-height: 64px;
    color: var(--ink);
  }
  .company-reg {
    position: absolute;
    left: 0;
    top: 230px;
    width: 1040px;
    text-align: center;
    font-weight: 600;
    font-size: 24px;
    line-height: 34px;
  }
  .divider {
    position: absolute;
    left: 110px;
    top: 295px;
    width: 820px;
    height: 5px;
    border-radius: 3px;
    background: linear-gradient(90deg, rgba(255,255,255,0) 0%, var(--white) 12%, var(--white) 88%, rgba(255,255,255,0) 100%);
  }
  .service {
    position: absolute;
    margin: 0;
    font-weight: 500;
    font-size: 25px;
    line-height: 34px;
    letter-spacing: 0.3px;
  }
  .service::after, .service::before {
    position: absolute;
    top: 6px;
    width: 24px;
    height: 24px;
    border-radius: 50%;
    background: var(--bullet);
  }
  .services-left .service {
    right: 623px;
    text-align: right;
    white-space: nowrap;
  }
  .services-left .service::after {
    content: "";
    right: -33px;
  }
  .services-right .service {
    left: 585px;
    white-space: nowrap;
  }
  .services-right .service::before {
    content: "";
    left: -28px;
  }
  .rate-band {
    position: absolute;
    left: 0;
    top: 1064px;
    width: 1040px;
    height: 118px;
    background: var(--band);
    box-shadow: 0 -6px 10px rgba(90,110,90,0.35), 0 6px 10px rgba(90,110,90,0.35);
    display: flex;
    flex-direction: column;
    justify-content: center;
    align-items: center;
  }
  .rate-band p {
    margin: 0;
    font-weight: 700;
    font-size: 27px;
    line-height: 34px;
  }
  .callout-shape {
    position: absolute;
    left: 0;
    top: 0;
  }
  .callout-text {
    position: absolute;
    left: 0;
    top: 1280px;
    width: 1040px;
    text-align: center;
    color: var(--white);
    font-weight: 500;
    font-size: 25px;
    line-height: 34px;
    margin: 0;
  }
</style>
</head>
<body>
<div class="stage">
  <div class="flyer">
    <h1 class="company-name">Brightlink Home Tech Pty Ltd</h1>
    <div class="company-reg">ABN - 12 345 678 901 Established 2002</div>
    <div class="divider"></div>

    <div class="services-left">
      <p class="service" style="top:395px">Home Network &amp; Wireless setup</p>
      <p class="service" style="top:463px">Improvements for extending<br>your home Wireless</p>
      <p class="service" style="top:566px">IP Camera installations –<br>external and internal</p>
      <p class="service" style="top:669px">Backup solutions either at<br>home or to a cloud provider</p>
      <p class="service" style="top:771px">Computer &amp; Network Security</p>
      <p class="service" style="top:840px">Email setup</p>
      <p class="service" style="top:908px">Domain setup and<br>email migration to cloud</p>
    </div>

    <div class="services-right">
      <p class="service" style="top:396px">Media streamer installations and<br>wireless setup –Stream movies and<br>shows to your existing TV</p>
      <p class="service" style="top:533px">Computer Setup</p>
      <p class="service" style="top:601px">New computer recommendations</p>
      <p class="service" style="top:670px">New computer unpacking and<br>setup</p>
      <p class="service" style="top:772px">Mobile phone setups and training</p>
      <p class="service" style="top:841px">Computer training</p>
      <p class="service" style="top:909px">Telephony &amp;Network Cable<br>relations and installations</p>
    </div>

    <div class="rate-band">
      <p>We charge $70 Ex GST per hour. (All major credit cards accepted)</p>
      <p>We can procure all new hardware and provide you obligation free quotes.</p>
    </div>

    <svg class="callout-shape" width="1040" height="1477" viewBox="0 0 1040 1477" aria-hidden="true">
      <defs>
        <filter id="soft-shadow" x="-10%" y="-30%" width="120%" height="160%">
          <feDropShadow dx="0" dy="4" stdDeviation="6" flood-color="#556655" flood-opacity="0.45"/>
        </filter>
      </defs>
      <polygon points="100,1252 940,1252 1022,1339 940,1427 100,1427 18,1339" fill="var(--frame)" filter="url(#soft-shadow)"/>
      <polygon points="165,1252 875,1252 943,1339 875,1427 165,1427 97,1339" fill="var(--cyan)"/>
    </svg>
    <p class="callout-text">No job is too small, please call or<br>email our team who will be happy to assist<br>with your enquiry and schedule an appointment.<br>We can also accommodate afterhours appointments.</p>
  </div>
</div>
</body>
</html>
```